What makes us Different Managed Communications Services Provider Flyer

We need a flyer to explain why we are different than other "managed IT services" company. Gives a brief description of our company and services that can entice clients and potential clients to setup a FREE consultation with us. This will become part of an ongoing marketing campaign that includes emails, leave behinds, brochures, and more

```html
<!DOCTYPE html>
<html lang="en">
<head>
<meta charset="utf-8">
<title>Managed IT Services Flyer</title>
<link href="https://fonts.googleapis.com/css2?family=Jost:wght@400;500;600;700&display=swap" rel="stylesheet">
<style>
  :root {
    --backdrop: #c9c9c9;
    --paper: #ffffff;
    --ink: #111111;
    --body-ink: #1d1d1d;
    --blue-deep: #1a55b0;
    --blue-bright: #2cb8ea;
    --bar-dark: #0b0b0b;
    --art-light: #e4f1fb;
    --art-mid: #9fd0f2;
  }
  * { box-sizing: border-box; margin: 0; padding: 0; }
  html, body { width: 1200px; height: 1200px; overflow: hidden; }
  body {
    background: var(--backdrop);
    font-family: "Jost", sans-serif;
    color: var(--body-ink);
    position: relative;
  }
  .flyer {
    position: absolute;
    left: 190px; top: 20px;
    width: 820px; height: 1160px;
    background: var(--paper);
    overflow: hidden;
  }
  .flyer-title {
    position: absolute; left: 42px; top: 50px;
    font-size: 35px; font-weight: 700; color: var(--ink);
    letter-spacing: 0.3px;
  }
  .brand-mark {
    position: absolute; left: 576px; top: 140px;
    display: flex; align-items: center; gap: 10px;
    white-space: nowrap;
  }
  .brand-mark .square {
    width: 22px; height: 22px; background: var(--blue-deep);
  }
  .brand-mark .name {
    font-size: 23px; font-weight: 500; color: var(--ink);
  }
  .hero-art {
    position: absolute; left: 410px; top: 195px;
    width: 372px; height: 285px;
    background: radial-gradient(ellipse at 50% 60%, var(--art-mid) 0%, var(--art-light) 70%, var(--paper) 100%);
    border-radius: 8px;
  }
  .band {
    position: absolute;
    background: linear-gradient(90deg, var(--blue-deep), var(--blue-bright));
    color: #fff;
    font-size: 20px; font-weight: 600; line-height: 23px;
    display: flex; align-items: center;
    padding-right: 16px;
  }
  .band.left { left: 0; padding-left: 42px; }
  .band.right { padding-left: 15px; }
  .copy {
    position: absolute;
    font-size: 14.2px; line-height: 19.6px;
    text-align: justify; hyphens: auto;
  }
  .copy p + p { margin-top: 19.6px; }
  .copy ul { list-style: none; margin-top: 2px; }
  .copy li {
    position: relative; padding-left: 27px; text-align: left;
    line-height: 18px;
  }
  .copy li::before {
    content: ""; position: absolute; left: 14px; top: 8px;
    width: 4px; height: 4px; border-radius: 50%; background: var(--body-ink);
  }
  .cta {
    position: absolute; left: 42px; top: 1070px;
    font-size: 34px; font-weight: 600; color: var(--ink);
  }
  .footer-bar {
    position: absolute; left: 0; bottom: 0; width: 100%; height: 18px;
  }
  .footer-bar .blue {
    position: absolute; left: 0; top: 0; width: 340px; height: 100%;
    background: linear-gradient(90deg, var(--blue-deep), var(--blue-bright));
  }
  .footer-bar .dark {
    position: absolute; left: 340px; top: 0; width: 338px; height: 100%;
    background: var(--bar-dark);
  }
</style>
</head>
<body>
<main class="flyer">
  <h1 class="flyer-title">MANAGED IT SERVICES</h1>

  <div class="brand-mark">
    <span class="square"></span>
    <span class="name">Northline Systems</span>
  </div>

  <div class="hero-art" role="img" aria-label="Illustration of a team working around a large laptop with cloud, security and data icons"></div>

  <h2 class="band left" style="top:127px;width:377px;height:84px;">More Than Just a Managed IT<br>Provider – Our Legacy of<br>Excellence</h2>
  <div class="copy" style="left:42px;top:214px;width:355px;">
    <p>At our company, we are far more than your typical managed IT provider. Since our founding in 1983, we have built a reputation based on trust, reliability, and unparalleled service. With client relationships spanning 20 to 30 years, we have demonstrated a level of commitment that few IT firms can match. What sets us apart is not just our technical expertise but the deep, long-term partnerships we cultivate with our clients—many of whom have stayed with us without ever being locked into a contract. That is a testament to the exceptional quality of our service and the trust we have earned over decades.</p>
  </div>

  <h2 class="band left" style="top:456px;width:405px;height:42px;">A Commitment Beyond Contracts</h2>
  <div class="copy" style="left:42px;top:516px;width:355px;">
    <p>Unlike many managed IT providers who rely on rigid contracts to retain clients, we believe that service excellence speaks for itself. The longevity of our client relationships is rooted in our ability to anticipate needs, resolve challenges before they escalate, and proactively enhance network &amp; communication infrastructures. Our comprehensive checklists, questionnaires, policies, and procedures, attention to details ensure that every client receives a tailored, best-in-class experience from day one.</p>
  </div>

  <h2 class="band left" style="top:727px;width:340px;height:62px;">A Holistic Approach to IT<br>Management</h2>
  <div class="copy" style="left:42px;top:802px;width:355px;">
    <p>We don’t just manage IT—we integrate ourselves into your business, ensuring that technology aligns with your strategic goals. Our services go beyond traditional break-fix support; we offer:</p>
    <ul>
      <li>Strategic IT Roadmaps customized to drive business growth.</li>
      <li>Proactive cybersecurity assessments that help keep businesses secure.</li>
      <li>Comprehensive backup and disaster recovery solutions that provide peace of mind.</li>
      <li>Industry-leading response times and dedicated support teams focused on delivering an exceptional client experience.</li>
    </ul>
  </div>

  <p class="cta">FREE consultation</p>

  <h2 class="band right" style="left:410px;top:504px;width:368px;height:62px;">Our Clients Stay Because<br>We Deliver</h2>
  <div class="copy" style="left:424px;top:583px;width:354px;">
    <p>For over 40 years, we have maintained a standard of excellence that other companies simply cannot compare with. Our team of experts consistently goes above and beyond, ensuring that clients not only get the support they need but also receive the strategic guidance necessary to stay ahead in an ever-evolving digital landscape.</p>
    <p>Our 90-day performance review process ensures that we continuously improve our service based on client feedback. This process allows us to adapt, refine, and enhance our approach, providing a truly personalized IT experience that aligns with business objectives.</p>
  </div>

  <h2 class="band right" style="left:410px;top:853px;width:368px;height:38px;">A Legacy of Trust &amp; Reliability</h2>
  <div class="copy" style="left:424px;top:905px;width:354px;">
    <p>The fact that many of our clients have remained with us for decades without a formal contract speaks volumes about the trust we have built. We don’t lock in clients with paperwork—we keep them with results. That’s the difference between a standard managed IT provider and an IT partner who genuinely cares.</p>
    <p>If you’re looking for an IT provider that will treat your business as if it were their own, look no further. Our legacy of service, innovation, and commitment to our clients is what sets us apart from the rest.</p>
  </div>

  <div class="footer-bar">
    <span class="blue"></span>
    <span class="dark"></span>
  </div>
</main>
</body>
</html>
```